Stylish new business card needed!

Hello everyone! I am in need of a new business card design for an alarm company here in Hurricane WV. I have all fonts, color codes and logos provided for you use! We are a young company and like the style of a clean sleek looking business card. Would like it double sided, one side holding the logo and the other with your design!
Target Market(s)
The people that are looking for the newest tech for home automation and security
Industry/Entity Type
Alarm services; Home automation
Contact Information for Business Card
Name of person; position (Sales; Installer); Phone Number (555.419.7362); Employee cell Number; Website (www.GuardedByVelm.example); Employee Email; Double sided
Look and feel
Each slider illustrates characteristics of the customer's brand and the style your logo design should communicate.

```html
<!DOCTYPE html>
<html lang="en">
<head>
<meta charset="utf-8">
<title>VELM Business Card</title>
<link rel="stylesheet" href="https://fonts.googleapis.com/css2?family=Montserrat:wght@400;500&display=swap">
<style>
  :root {
    --backdrop: #f1f1f1;
    --card: #ffffff;
    --grey: #949494;
    --grey-text: #8a8a8a;
    --orange: #f28c4e;
  }
  * { margin: 0; padding: 0; box-sizing: border-box; }
  html, body {
    width: 1200px;
    height: 1200px;
    overflow: hidden;
    background: var(--backdrop);
    font-family: "Montserrat", Arial, sans-serif;
  }
  .card {
    position: absolute;
    left: 178px;
    width: 845px;
    height: 498px;
    background: var(--card);
  }
  .card--front { top: 85px; }
  .card--back { top: 616px; }

  .brand {
    position: absolute;
    display: flex;
    align-items: center;
    gap: 16px;
  }
  .brand__name {
    font-size: 165px;
    font-weight: 400;
    line-height: 1;
    color: var(--grey);
    letter-spacing: -4px;
  }
  .brand__dot {
    width: 30px;
    height: 30px;
    border-radius: 50%;
    background: var(--orange);
    margin-top: 60px;
  }
  .card--front .brand { left: 60px; top: 72px; }
  .card--back .brand { left: 74px; top: 266px; }

  .person {
    position: absolute;
    left: 68px;
    top: 276px;
    color: var(--grey-text);
  }
  .person__name {
    font-size: 26px;
    font-weight: 500;
    letter-spacing: 1.5px;
    line-height: 1.2;
    text-transform: uppercase;
  }
  .person__role {
    font-size: 22px;
    font-weight: 400;
    margin-top: 4px;
  }

  .contact {
    position: absolute;
    right: 52px;
    top: 298px;
    list-style: none;
    color: var(--grey-text);
    font-size: 20px;
  }
  .contact__item {
    display: flex;
    justify-content: flex-end;
    align-items: center;
    gap: 14px;
    height: 32px;
  }
  .contact__item--address { margin-top: 17px; }
  .contact__icon { width: 18px; height: 18px; flex: none; }
</style>
</head>
<body>

<section class="card card--front">
  <div class="brand">
    <span class="brand__name">VELM</span>
    <span class="brand__dot"></span>
  </div>

  <div class="person">
    <p class="person__name">Daniel<br>Harrow</p>
    <p class="person__role">CEO, President</p>
  </div>

  <ul class="contact">
    <li class="contact__item">
      <span>555.419.7362</span>
      <svg class="contact__icon" viewBox="0 0 24 24" fill="none" stroke="#f28c4e" stroke-width="2" stroke-linejoin="round"><path d="M5 3h4l2 5-2.5 1.5a11 11 0 0 0 6 6L16 13l5 2v4a2 2 0 0 1-2 2A17 17 0 0 1 3 5a2 2 0 0 1 2-2z"/></svg>
    </li>
    <li class="contact__item">
      <span>info@velm.example</span>
      <svg class="contact__icon" viewBox="0 0 24 24"><rect x="2" y="5" width="20" height="14" fill="#f28c4e"/><path d="M2 5l10 8 10-8" fill="none" stroke="#fff" stroke-width="1.8"/></svg>
    </li>
    <li class="contact__item">
      <span>www.GuardedByVelm.example</span>
      <svg class="contact__icon" viewBox="0 0 24 24" fill="none" stroke="#f28c4e" stroke-width="2"><circle cx="12" cy="12" r="9"/><path d="M3 12h18M12 3c3 3 3 15 0 18M12 3c-3 3-3 15 0 18"/></svg>
    </li>
    <li class="contact__item contact__item--address">
      <span>42 Linden Rd Marlow NV 8841</span>
      <svg class="contact__icon" viewBox="0 0 24 24" fill="none" stroke="#f28c4e" stroke-width="2"><path d="M12 21s-6-6.5-6-11a6 6 0 0 1 12 0c0 4.5-6 11-6 11z"/><circle cx="12" cy="10" r="2.2"/></svg>
    </li>
  </ul>
</section>

<section class="card card--back">
  <div class="brand">
    <span class="brand__name">VELM</span>
    <span class="brand__dot"></span>
  </div>
</section>

</body>
</html>
```